Honey Jar Label Design

I am looking for a fun label design for a 1 lb honey jar.
The company is Corliss Waverly Botanicals, which sells cut flowers and is expanding into honey and eventually other honey products. I've included the design work for the business, and I'd like the honey products to coordinate with them but not necessarily match directly.
Label requirements:
Raw Honey
Corliss Waverly Botanicals
27308 Quarry Bend Rd
Ashgrove, MO 66341
NET WT. 16 OZ. (weight info must be in the lower third of the front label and easy to read)
Look and feel
Each slider illustrates characteristics of the customer's brand and the style your logo design should communicate.

```html
<!DOCTYPE html>
<html lang="en">
<head>
<meta charset="utf-8">
<title>Raw Honey Label – Corliss Waverly Botanicals</title>
<link rel="stylesheet" href="https://fonts.googleapis.com/css2?family=Playfair+Display:wght@400&family=Montserrat:wght@400;500&display=swap">
<style>
  :root {
    --ink-teal: #0f2a33;
    --blush: #e7d4d3;
    --paper: #ffffff;
  }
  html, body {
    margin: 0;
    padding: 0;
    width: 1200px;
    height: 1200px;
    overflow: hidden;
    background: var(--paper);
  }
  .canvas {
    position: relative;
    width: 1200px;
    height: 1200px;
  }
  .shapes {
    position: absolute;
    inset: 0;
  }
  .label-text {
    position: absolute;
    left: 210px;
    width: 402px;
    text-align: center;
    color: var(--blush);
    margin: 0;
  }
  .seal-name {
    top: 470px;
    font-family: "Montserrat", sans-serif;
    font-weight: 400;
    font-size: 9px;
    letter-spacing: 1.5px;
    line-height: 13px;
    text-transform: uppercase;
  }
  .product-title {
    top: 578px;
    font-family: "Playfair Display", serif;
    font-weight: 400;
    font-size: 72px;
    line-height: 70px;
    letter-spacing: 2px;
  }
  .brand-name {
    top: 730px;
    font-family: "Montserrat", sans-serif;
    font-weight: 400;
    font-size: 18px;
    line-height: 24px;
    letter-spacing: 2.6px;
    text-transform: uppercase;
  }
  .address {
    top: 871px;
    font-family: "Montserrat", sans-serif;
    font-weight: 400;
    font-size: 14.5px;
    line-height: 19px;
  }
  .net-weight {
    top: 931px;
    font-family: "Montserrat", sans-serif;
    font-weight: 500;
    font-size: 18.5px;
    line-height: 24px;
    letter-spacing: 0.3px;
  }
  .bee-art {
    position: absolute;
    left: 380px;
    top: 800px;
    width: 62px;
    height: 50px;
    border-radius: 50%;
    background: radial-gradient(ellipse at center, rgba(231,212,211,0.55), rgba(231,212,211,0.08) 70%, transparent);
  }
  .sticker-name {
    position: absolute;
    left: 820px;
    top: 640px;
    width: 242px;
    text-align: center;
    margin: 0;
    color: var(--blush);
    font-family: "Playfair Display", serif;
    font-weight: 400;
    font-size: 34px;
    line-height: 36px;
  }
</style>
</head>
<body>
<main class="canvas">
  <svg class="shapes" width="1200" height="1200" viewBox="0 0 1200 1200" aria-hidden="true">
    <path class="jar-label" d="M345 375 H476 C500 375 510 385 520 400 C590 520 612 700 606 980 C605 1005 590 1016 566 1016 H255 C231 1016 216 1005 215 980 C209 700 231 520 301 400 C311 385 321 375 345 375 Z"
          fill="var(--ink-teal)" stroke="var(--blush)" stroke-width="12" stroke-linejoin="round"/>
    <circle class="seal-ring" cx="411" cy="489" r="54" fill="none" stroke="var(--blush)" stroke-width="0.8"/>
    <circle class="round-sticker" cx="941" cy="694" r="138" fill="var(--ink-teal)" stroke="var(--blush)" stroke-width="6"/>
  </svg>

  <p class="label-text seal-name">Corliss<br>Waverly<br>Botanicals</p>
  <h1 class="label-text product-title">RAW<br>HONEY</h1>
  <p class="label-text brand-name">Corliss Waverly<br>Botanicals</p>
  <div class="bee-art" role="img" aria-label="Fine line engraving of a honey bee"></div>
  <p class="label-text address">27308 Quarry Bend Rd<br>Ashgrove, MO 66341</p>
  <p class="label-text net-weight">NET WT. 16 OZ.</p>

  <p class="sticker-name">Corliss<br>Waverly<br>Botanicals</p>
</main>
</body>
</html>
```